Postcard for Real estate agent

**Scroll all the way down for updates***.....
I want a postcard to send out to potential clients to list their house on the market.
I submitting a a basic proof with the info and images that I want on each side of the postcard. I do not want a white postcard
-I want the postcard sized 6" x 4" inches
I want my phone number to stand out
I want a PHD and Homewarden log on my postcard .Ive included examples of logos.
Feel free toe crop or enhance the images
Must look professional
-----------------------------------------------------------------------
UPDATE : August 4 , 2015 8pm Pacific Daylight Time , UTC -7
I submitted a proof of postcard I designed myself (see File 10)
Please use that for the front of the postcard.
For the back please refine the back to make it look professional
(see example of File 11 )
-----------------------------------------------------------------------------------------------------------
UPDATE: August 5 12:45 pm Pacific Daylight Time (UTC -7)
Please use Files 12, 13 and 14 on the front. No generic pictures.
You may crop and enhance my images if needed.
On the back, bottom of the postcard must have "If you are listed with another broker please disregard this mailing. This is not a solicitation"
UPDATE: August 5 12:45 pm Pacific Daylight Time (UTC -7)-------------------------------------------------------------------------------------Please use new Files 12, 13 and 14 on the front. No generic pictures.You may crop and enhance my images if needed.On the back, bottom of the postcard must have "If you are listed with another broker please disregard this mailing. This is not a solicitation"Upper left must have return address : 482 Pellmore Ave #C Avalon CA 90617-5083 Added Wednesday, August 5, 2015
Homeowners wanting to sell their property
Real Estate Agent
- My name and phone number highly visible
- Homewarden/ PHD logo
- Nothing pink, purple, lavender, brown , no pastels

```html
<!DOCTYPE html>
<html lang="en">
<head>
<meta charset="utf-8">
<title>Dana Whitcomb – Listing Postcard</title>
<link rel="stylesheet" href="https://fonts.googleapis.com/css2?family=Cinzel:wght@700&family=Oswald:wght@400;500&family=Roboto+Condensed:wght@400;700&display=swap">
<style>
  :root {
    --page: #d9dadc;
    --ink-dark: #1f232b;
    --accent-red: #d8262c;
    --paper: #ffffff;
    --back-paper: #eceef0;
    --text-grey: #3a3d42;
    --photo-green: #5f7f45;
    --photo-stone: #c9bfae;
  }
  * { box-sizing: border-box; margin: 0; padding: 0; }
  html, body { width: 900px; height: 1200px; overflow: hidden; }
  body { background: var(--page); position: relative; font-family: "Roboto Condensed", sans-serif; }

  .postcard {
    position: absolute; left: 40px; width: 820px; height: 547px;
    overflow: hidden; background: var(--paper);
  }
  .postcard--front { top: 40px; }
  .postcard--back { top: 620px; background: var(--back-paper); }
  .postcard__art { position: absolute; inset: 0; width: 100%; height: 100%; }

  .brand-row { position: absolute; top: 22px; left: 22px; display: flex; align-items: center; gap: 18px; }
  .brand {
    font-family: "Roboto Condensed", sans-serif; font-weight: 400;
    color: var(--ink-dark); font-size: 16px; letter-spacing: 0.5px;
  }
  .brand-row--small { top: 18px; gap: 12px; }
  .brand-row--small .brand { font-size: 12px; }

  .agent-tag {
    position: absolute; left: 570px; top: 268px; width: 150px; padding: 4px 0;
    background: var(--accent-red); color: var(--paper); text-align: center;
    font-size: 13px; line-height: 1.15;
  }
  .front-pitch { position: absolute; left: 0; right: 0; top: 392px; text-align: center; }
  .front-pitch__question { font-family: "Cinzel", serif; font-weight: 700; font-size: 34px; color: var(--accent-red); }
  .front-pitch__phone { margin-top: 8px; font-family: "Oswald", sans-serif; font-size: 34px; color: var(--paper); letter-spacing: 0.5px; }

  .back-contact { position: absolute; left: 40px; top: 330px; font-size: 16px; line-height: 1.25; color: var(--accent-red); }
  .back-contact__name, .back-contact__phone { font-weight: 700; font-size: 18px; }
  .back-contact__office { margin-top: 16px; }
  .back-web { position: absolute; left: 220px; top: 455px; font-size: 14px; line-height: 1.3; color: var(--text-grey); text-align: right; }
</style>
</head>
<body>

<section class="postcard postcard--front">
  <svg class="postcard__art" viewBox="0 0 820 547">
    <defs>
      <linearGradient id="homePhoto" x1="0" y1="0" x2="0" y2="1">
        <stop offset="0" stop-color="#8c8a80"/>
        <stop offset="0.45" stop-color="#c9bfae"/>
        <stop offset="1" stop-color="#5f7f45"/>
      </linearGradient>
      <linearGradient id="agentPhoto" x1="0" y1="0" x2="0" y2="1">
        <stop offset="0" stop-color="#e6e2dc"/>
        <stop offset="1" stop-color="#b9a48a"/>
      </linearGradient>
    </defs>
    <rect x="0" y="0" width="820" height="380" fill="url(#homePhoto)" role="img" aria-label="Photo of the two-storey apartment home with balconies and a tropical garden"/>
    <path d="M0 0 H380 C260 25 120 60 0 120 Z" fill="#ffffff"/>
    <path d="M0 345 C250 312 520 282 820 228 V250 C520 300 250 332 0 362 Z" fill="#ffffff"/>
    <path d="M0 352 C250 320 520 290 820 238 V262 C520 310 250 340 0 372 Z" fill="#d8262c"/>
    <path d="M0 372 C250 340 520 310 820 262 V547 H0 Z" fill="#1f232b"/>
    <circle cx="645" cy="205" r="84" fill="url(#agentPhoto)" stroke="#ffffff" stroke-width="8" role="img" aria-label="Portrait of the agent"/>
  </svg>

  <div class="brand-row">
    <span class="brand brand--homewarden">Homewarden</span>
    <span class="brand brand--phd">PHD</span>
  </div>

  <div class="agent-tag">Dana Whitcomb<br>Harborview Realtors</div>

  <div class="front-pitch">
    <h1 class="front-pitch__question">Thinking of selling?</h1>
    <p class="front-pitch__phone">Call me today 310 555 0148</p>
  </div>
</section>

<section class="postcard postcard--back">
  <svg class="postcard__art" viewBox="0 0 820 547">
    <path d="M260 0 H820 V70 C620 40 430 25 260 0 Z" fill="#1f232b"/>
    <path d="M250 0 C430 28 620 44 820 74 V84 C620 54 430 36 250 0 Z" fill="#d8262c"/>
    <path d="M0 500 C180 520 320 535 430 547 H0 Z" fill="#d8262c"/>
    <line x1="440" y1="60" x2="440" y2="500" stroke="#b9bcc0" stroke-width="2"/>
    <rect x="680" y="100" width="80" height="96" fill="none" stroke="#1f232b" stroke-width="3"/>
    <circle cx="130" cy="240" r="72" fill="#8a8a6e" stroke="#ffffff" stroke-width="6" role="img" aria-label="Photo of the office entrance with a for-sale sign"/>
    <circle cx="262" cy="168" r="50" fill="#7e9a9e" stroke="#ffffff" stroke-width="6" role="img" aria-label="Photo of a home with a pool"/>
  </svg>

  <div class="brand-row brand-row--small">
    <span class="brand brand--homewarden">Homewarden</span>
    <span class="brand brand--phd">PHD</span>
  </div>

  <div class="back-contact">
    <p class="back-contact__name">Dana Whitcomb</p>
    <p class="back-contact__phone">Call (310) 555-0148</p>
    <p class="back-contact__office">Harborview Realtors<br>Glen Marsh, Broker</p>
  </div>

  <div class="back-web">
    <p>sales@danawhitcomb.com</p>
    <p>www.HarborviewRealtors.com</p>
  </div>
</section>

</body>
</html>
```